Business card design needed

I would like to use the print I have supplied with my Logo & info i have supplied.
On the back i would like a
*We Use & Recommend*
*Tarvin Filters
*Dulmok Oils
*QRV Spark Plugs
*Z-Blade Exhaust
*Colvane Brake Pads

*Your Next Appointment:

Industry/Entity Type

Business

Contact Information for Business Card

FERRIMS AUTO CENTRE
All Mechanical Repairs
Log Book Servicing
Authorised NSW Inspection station
Email: ferrimsautocentre@mailbox-example.com.au
17 Tumbrel Rd
P.O.Box 8270
Queanbeyan NSW 2629
0262480315

```html
<!DOCTYPE html>
<html lang="en">
<head>
<meta charset="utf-8">
<title>Ferrims Auto Centre – Business Card</title>
<link rel="stylesheet" href="https://fonts.googleapis.com/css2?family=Josefin+Slab:wght@400;600&display=swap">
<style>
  :root {
    --backdrop-light: #f4ece6;
    --backdrop-peach: #e9c9b6;
    --panel-dark: #1f1b1a;
    --panel-rust: #5a2a1e;
    --panel-mid: #3a302d;
    --glow: rgba(255, 255, 255, 0.28);
    --rule: #c9c5c2;
    --text-light: #d9d4cf;
    --brand-silver: #e6eaee;
  }
  * { margin: 0; padding: 0; box-sizing: border-box; }
  html, body {
    width: 1200px;
    height: 741px;
    overflow: hidden;
    background: var(--backdrop-light);
  }
  .card {
    position: relative;
    width: 1200px;
    height: 741px;
    font-family: "Josefin Slab", Georgia, serif;
    color: var(--text-light);
  }
  .backdrop-art {
    position: absolute;
    inset: 0;
    background:
      radial-gradient(ellipse 60% 30% at 30% 4%, var(--backdrop-peach), transparent 70%),
      radial-gradient(ellipse 40% 40% at 2% 70%, #e4d8d2, transparent 70%),
      linear-gradient(180deg, var(--backdrop-light), #efe6e1);
  }
  .panel {
    position: absolute;
    left: 49px;
    top: 30px;
    width: 1113px;
    height: 686px;
    border-radius: 18px;
    overflow: hidden;
    background: var(--panel-dark);
  }
  .panel-art {
    position: absolute;
    inset: 0;
    background:
      radial-gradient(ellipse 22% 16% at 53% 36%, var(--glow), transparent 75%),
      radial-gradient(ellipse 55% 40% at 45% 55%, rgba(110, 45, 30, 0.75), transparent 75%),
      radial-gradient(ellipse 45% 30% at 30% 18%, rgba(90, 40, 28, 0.7), transparent 75%),
      radial-gradient(ellipse 35% 35% at 88% 80%, rgba(70, 65, 62, 0.7), transparent 75%),
      linear-gradient(180deg, var(--panel-mid), var(--panel-rust) 55%, var(--panel-dark));
  }
  .brand {
    position: absolute;
    left: 0;
    right: 0;
    top: 248px;
    text-align: center;
    font-weight: 600;
    font-size: 58px;
    letter-spacing: 4px;
    color: var(--brand-silver);
  }
  .rule {
    position: absolute;
    left: 0;
    width: 100%;
    height: 5px;
    background: var(--rule);
  }
  .rule--upper { top: 399px; }
  .rule--lower { top: 412px; }
  .details {
    position: absolute;
    top: 448px;
    list-style: none;
    font-size: 27px;
    line-height: 49px;
    letter-spacing: -0.3px;
  }
  .details--services { left: 42px; }
  .details--contact { left: 657px; }
  .details .email { font-size: 22px; }
</style>
</head>
<body>
  <div class="card">
    <div class="backdrop-art" role="img" aria-label="Faded illustration of a classic muscle car behind the card"></div>
    <section class="panel">
      <div class="panel-art" role="img" aria-label="Illustration of two classic red sedans on a dark background with a light glow behind the name"></div>
      <h1 class="brand">FERRIMS AUTO CENTRE</h1>
      <div class="rule rule--upper"></div>
      <div class="rule rule--lower"></div>
      <ul class="details details--services">
        <li>FERRIMS AUTO CENTRE,</li>
        <li>All Mechanical Repairs,</li>
        <li>Log Book Servicing</li>
        <li>Authorised NSW Inspection Station.</li>
      </ul>
      <ul class="details details--contact">
        <li class="email">Email:ferrimsautocentre@mailbox-example.com.au</li>
        <li>17 Tumbrel Rd&nbsp; P.O.Box 8270,</li>
        <li>Queanbeyan NSW&nbsp; 2629 0262480315</li>
      </ul>
    </section>
  </div>
</body>
</html>
```